Business Cards for IT Consulting Company (Managed Service Provider)

I am looking to have some business cards printed and would like some designs. We are an IT Consulting company based in Vancouver BC. I would like a nice clean and modern look to the cards. I have uploaded all the versions of my logo so parts can be used as needed. Here is a snippit from our website homepage:

Kelbrook Systems Ltd. is an IT Solutions Partner located in Vancouver BC, Canada. We offer IT solutions and support to customers in the greater Vancouver Area. With expertise in Microsoft platforms, as well as Linux and Mac OSX and over 12 years experience in the IT industry, Kelbrook Systems is dedicated to offering our clients top quality service and products. We take pride in the solutions we offer our customers. The greatest compliment a client can give us is to recommend our services.

Kelbrook Systems Ltd. offers a wide range of IT services from onsite service to remote support and managed service solutions. This allows clients to choose the support path that best suits their company’s needs. Supporting many different sized companies from small to enterprise level over the past 12 years Kelbrook Systems has the experience and expertise needed to ensure things run smoothly. Allowing our clients to focus on doing business.

Revolutionizing the way IT services are delivered.

Kelbrook Systems is dedicated to providing our clients with IT solutions that work and grow with them for years to come. This philosophy helps save money in the long run instead of replacing equipment constantly. Far too often IT solutions are not well thought out and while possibly solving the problem at hand, require replacement due to growth or quality within a very short time frame. Kelbrook Systems takes pride in providing solutions that will last and be able to accommodate growth without the need for replacement.

Industry/Entity Type

Information Technology

Contact Information for Business Card

Kelbrook Systems Ltd.
(Employee Name)
Eml: (Employees Email Address)
Web: kelbrook.me
Ph: 604-555-0142

Font styles to use
Serif
Sans Serif

Requirements
Must have
• The Company logo and company colors.
Nice to have
• - Our tag line: "Revolutionizing IT Services" or "Revolutionizing the way IT services are delivered."
• - Also I really like the idea of nature and technology together blending which is sort of where my logo came from so integrating that somehow onto the business cards would be great.

```html
<!DOCTYPE html>
<html lang="en">
<head>
<meta charset="utf-8">
<title>Kelbrook Systems Ltd. — Business Cards</title>
<link rel="stylesheet" href="https://fonts.googleapis.com/css2?family=Montserrat:wght@500;700;800&family=Open+Sans:wght@400;600;700&display=swap">
<style>
  :root {
    --canvas: #e9e9e7;
    --card-dark: #111817;
    --card-dark-2: #1c2422;
    --card-light: #ffffff;
    --brand-blue: #1eaee8;
    --text-grey: #5f6163;
    --text-soft: #e8e8e8;
    --shadow: rgba(0, 0, 0, 0.28);
  }
  * { box-sizing: border-box; margin: 0; padding: 0; }
  html, body {
    width: 1200px; height: 1200px; overflow: hidden;
    background: var(--canvas);
  }
  .stage { position: relative; width: 1200px; height: 1200px; }

  .card {
    position: absolute;
    width: 720px; height: 411px;
    border-radius: 4px;
    box-shadow: 0 14px 30px var(--shadow);
    overflow: hidden;
  }

  /* Back of card */
  .card--back { left: 110px; top: 140px; background: var(--card-dark); }
  .card-back__pattern {
    position: absolute; inset: 0;
    background: radial-gradient(ellipse at 55% 40%, var(--card-dark-2), var(--card-dark) 75%);
  }
  .card-back__brand {
    position: absolute; left: 80px; top: 250px;
    display: flex; align-items: center; gap: 22px;
  }
  .brand-square {
    width: 86px; height: 86px;
    border: 5px solid var(--brand-blue);
  }
  .card-back__wordmark {
    font-family: "Montserrat", sans-serif;
    font-weight: 800;
    font-size: 34px;
    line-height: 1.05;
    color: var(--brand-blue);
  }
  .card-back__tagline {
    margin-top: 8px;
    font-family: "Montserrat", sans-serif;
    font-weight: 500;
    font-size: 16px;
    color: var(--text-soft);
    letter-spacing: 0.3px;
  }

  /* Front of card */
  .card--front { left: 370px; top: 640px; background: var(--card-light); }
  .card-front__brand {
    position: absolute; left: 52px; top: 150px; width: 300px;
    display: flex; align-items: center; gap: 16px;
  }
  .card-front__brand .brand-square { width: 46px; height: 46px; border-width: 3px; flex: none; }
  .card-front__wordmark {
    font-family: "Montserrat", sans-serif;
    font-weight: 800;
    font-size: 30px;
    line-height: 1.05;
    color: var(--brand-blue);
  }
  .card-front__divider {
    position: absolute; left: 380px; top: 100px;
    width: 3px; height: 210px; background: var(--brand-blue);
  }
  .card-front__person { position: absolute; left: 418px; top: 112px; }
  .person-name {
    font-family: "Montserrat", sans-serif;
    font-weight: 700; font-size: 25px;
    letter-spacing: 1.5px; text-transform: uppercase;
    color: var(--brand-blue);
  }
  .person-role {
    margin-top: 4px;
    font-family: "Open Sans", sans-serif;
    font-weight: 700; font-size: 14px;
    text-transform: uppercase; color: var(--text-grey);
  }
  .contact-list { list-style: none; margin-top: 26px; }
  .contact-item {
    display: flex; align-items: center; gap: 12px;
    font-family: "Open Sans", sans-serif;
    font-size: 15.5px; color: var(--text-grey);
    height: 26px;
  }
  .contact-icon {
    width: 18px; height: 18px; flex: none;
    background: var(--brand-blue); border-radius: 3px;
    display: flex; align-items: center; justify-content: center;
  }
  .contact-icon svg { width: 12px; height: 12px; }
</style>
</head>
<body>
<main class="stage">

  <section class="card card--back" aria-label="Card back">
    <div class="card-back__pattern" role="img" aria-label="Dark background with a subtle grey hexagon and cube line pattern"></div>
    <div class="card-back__brand">
      <div class="brand-square"></div>
      <div>
        <div class="card-back__wordmark">Kelbrook<br>Systems Ltd.</div>
        <div class="card-back__tagline">Revolutionizing IT Services</div>
      </div>
    </div>
  </section>

  <section class="card card--front" aria-label="Card front">
    <div class="card-front__brand">
      <div class="brand-square"></div>
      <div class="card-front__wordmark">Kelbrook<br>Systems Ltd.</div>
    </div>

    <div class="card-front__divider"></div>

    <div class="card-front__person">
      <div class="person-name">Dana Whitfield</div>
      <div class="person-role">Director</div>
      <ul class="contact-list">
        <li class="contact-item">
          <span class="contact-icon">
            <svg viewBox="0 0 12 12"><path d="M2.5 1.5l2 .3.6 2.3-1.2.8a6 6 0 0 0 3.2 3.2l.8-1.2 2.3.6.3 2a1 1 0 0 1-1 1A9 9 0 0 1 1.5 2.5a1 1 0 0 1 1-1z" fill="#fff"/></svg>
          </span>
          604-555-0142
        </li>
        <li class="contact-item">
          <span class="contact-icon">
            <svg viewBox="0 0 12 12"><rect x="3" y="0.8" width="6" height="10.4" rx="1" fill="none" stroke="#fff" stroke-width="1.2"/><circle cx="6" cy="9.3" r=".7" fill="#fff"/></svg>
          </span>
          604-555-0178
        </li>
        <li class="contact-item">
          <span class="contact-icon">
            <svg viewBox="0 0 12 12"><rect x="1" y="2.5" width="10" height="7" fill="none" stroke="#fff" stroke-width="1.2"/><path d="M1 2.8l5 4 5-4" fill="none" stroke="#fff" stroke-width="1.2"/></svg>
          </span>
          danawhitfield@kelbrook.me
        </li>
        <li class="contact-item">
          <span class="contact-icon">
            <svg viewBox="0 0 12 12"><circle cx="6" cy="6" r="4.8" fill="none" stroke="#fff" stroke-width="1.1"/><ellipse cx="6" cy="6" rx="2" ry="4.8" fill="none" stroke="#fff" stroke-width="1"/><path d="M1.2 6h9.6" stroke="#fff" stroke-width="1"/></svg>
          </span>
          kelbrook.me
        </li>
      </ul>
    </div>
  </section>

</main>
</body>
</html>
```